Our architectural studio needs a new business card

We need a business card design for our studio based in Waterloo in Belgium. We are active in architecture, design and installation.
Our works are contemporary and minimalist. our clients are refined and cultured.
Our business card must be minimalist and refined.

Project Deadline Extended
Reason: Some designers have accepted my invitation but they don't have all replied. I want to give them a chance to make one proposal. Paul

Target Market(s)

architecture

Industry/Entity Type

Business

Contact Information for Business Card

studio: paul dornevaux studio
paul dornevaux, architecte
M. +32 471 586 927
F. +322 619 4850
www.pauldornevaux-example.com
paul@pauldornevaux-example.com
14 rue des Marronniers
1420 Waterloo
Belgium

Font styles to use
Sans Serif

Requirements
Must have
• simple, minimalist, clear, elegant and chic! Black and white
Nice to have
• embossed logo, other format like a square for example
Should not have
• color, fantasy, curves, ...

```html
<!DOCTYPE html>
<html lang="fr">
<head>
<meta charset="utf-8">
<title>Paul Dornevaux Studio — Carte de visite</title>
<link rel="stylesheet" href="https://fonts.googleapis.com/css2?family=PT+Sans:wght@400;700&display=swap">
<style>
  :root {
    --backdrop: #e4e4e4;
    --paper: #ffffff;
    --ink: #151515;
    --card-black: #161616;
    --deboss: #3a3a3a;
  }
  * { margin: 0; padding: 0; box-sizing: border-box; }
  html, body {
    width: 1200px;
    height: 720px;
    overflow: hidden;
    background: var(--backdrop);
    font-family: "PT Sans", sans-serif;
    color: var(--ink);
  }
  .canvas { position: relative; width: 1200px; height: 720px; }
  .card {
    position: absolute;
    top: 242px;
    width: 420px;
    height: 238px;
  }
  .card--front { left: 147px; background: var(--paper); }
  .card--back  { left: 633px; background: var(--card-black); }

  .studio-mark {
    position: absolute;
    left: 31px;
    top: 22px;
    display: flex;
    align-items: center;
    gap: 7px;
    font-size: 13px;
    font-weight: 700;
    letter-spacing: 0.02em;
  }
  .studio-mark__square { width: 11px; height: 11px; background: var(--ink); }

  .person { position: absolute; left: 31px; top: 117px; }
  .person__name { font-size: 13.5px; font-weight: 700; line-height: 1.1; }
  .person__role { font-size: 10px; line-height: 1.3; }

  .contacts {
    position: absolute;
    left: 31px;
    top: 165px;
    list-style: none;
    font-size: 10.5px;
    line-height: 13px;
  }
  .contacts li { display: flex; align-items: center; gap: 6px; }
  .contacts svg { width: 11px; height: 9px; fill: var(--ink); flex: none; }

  .address {
    position: absolute;
    left: 259px;
    top: 191px;
    font-size: 10.5px;
    line-height: 13px;
    font-style: normal;
  }

  .back-name {
    position: absolute;
    left: 0;
    right: 0;
    top: 112px;
    text-align: center;
    color: var(--deboss);
    font-size: 11px;
    font-weight: 400;
    letter-spacing: 0.32em;
    text-transform: uppercase;
  }
</style>
</head>
<body>
<main class="canvas">
  <section class="card card--front" aria-label="Recto">
    <div class="studio-mark">
      <span class="studio-mark__square"></span>
      <span>paul dornevaux studio</span>
    </div>

    <div class="person">
      <p class="person__name">Paul Dornevaux</p>
      <p class="person__role">Architecte</p>
    </div>

    <ul class="contacts">
      <li>
        <svg viewBox="0 0 11 9" aria-hidden="true"><path d="M1 3.2C1 1.5 2.5 1 5.5 1S10 1.5 10 3.2L8.2 3.4 7.8 2.4H3.2L2.8 3.4Z"/><rect x="2.2" y="4" width="6.6" height="4.5" rx="0.6"/></svg>
        <span>+32 471 586 927</span>
      </li>
      <li>
        <svg viewBox="0 0 11 9" aria-hidden="true"><rect x="3" y="0.5" width="5" height="2.5"/><rect x="0.5" y="3" width="10" height="4" rx="0.6"/><rect x="3" y="6" width="5" height="2.6"/></svg>
        <span>+322 619 4850</span>
      </li>
      <li>
        <svg viewBox="0 0 11 9" aria-hidden="true"><path d="M0.5 1h10v7h-10z M1.5 2v0.3l4 3 4-3V2l-4 3z" fill-rule="evenodd"/></svg>
        <span>paul@pauldornevaux-example.com</span>
      </li>
      <li>
        <svg viewBox="0 0 11 9" aria-hidden="true"><path d="M0.8 0.8h9.4v6H0.8z M1.8 1.8v4h7.4v-4z" fill-rule="evenodd"/><rect x="3.5" y="7.4" width="4" height="1.2"/></svg>
        <span>www.pauldornevaux-example.com</span>
      </li>
    </ul>

    <address class="address">
      14 rue des Marronniers 1420<br>
      Waterloo Belgium
    </address>
  </section>

  <section class="card card--back" aria-label="Verso">
    <p class="back-name">paul dornevaux studio</p>
  </section>
</main>
</body>
</html>
```